Project Title:
Zembrix – Company Management Platform UI Design
Project Overview:
We are developing Zembrix, an all-in-one management platform for professional product and sales. The software combines daily operations, cost management, inventory, personnel administration, and planning into a single system.
We are launching this design competition to receive a clean, modern UI design that reflects the efficiency and structure of our system. This is not a Point of Sale (POS) system, but rather a back-office/administration tool used by product, sales, and office teams.
What we need:
A dashboard + 7 core module pages. The design should be dark, minimalist, and optimized for desktop views.
Dashboard Requirements:
The dashboard is the first screen after login. It should display:
• Due Dates
o Birthdays
o Passport expirations
o Contract expirations
o Residence permit expiration
o Missing documents / confirmations
o Vacation
o Illness
o Absence
o Warnings
o Terminations
o Maintenance
• Daily Routine
o Tasks
o Appointments
o Holidays & special days
o Vehicle logbook
o Deadlines
o To-do lists
o Weather
• Reports Shortcut
o Income and expenses
• Financial Overview
o Finances (income/expenses)
o Target-actual planning
o EBIT – target-actual
o OPDS documentation
o Loaned items
o Inventory
o Inventory price difference
o Contracts
o Reimbursements
o Travel expenses
7 Main Modules:
1. Activities – Daily closing, documentation, company data
2. Planning – Personnel, supplier, and service planning
3. Files – Personnel files, supplier data, service contracts
4. Costs – Personnel, supplier, and service costs
5. Finances – Income/expenses, EBIT balance sheet, liquidity overview
6. Product Goods – Inventory, price comparison, orders
7. API / Settings – Basic settings, interfaces, calendar, contacts
User Groups:
• Production roles: A, B, C…
• Office roles: A, B, C…
• Management: A, B, C…
Design Preferences:
• Style: Modern, minimalist, functional
• Theme: Dark/Light mode (standard and negative)
• Colors: Dark blue, gold/black accents, neon green
• Layout: Modular blocks, icons + labels, high readability, statistical charts
Deliverables:
• UI design files (Figma preferred, XD or Sketch acceptable)
• Static screens only (no prototype required)
• Up to 8 screens: 1 dashboard + 7 modules
Note:
This design will form the visual foundation of our product. We are looking for clearly structured, clean layouts that help companies manage their operations efficiently.

```html
<!DOCTYPE html>
<html lang="en">
<head>
<meta charset="utf-8">
<title>Zembrix – Dashboard</title>
<link href="https://fonts.googleapis.com/css2?family=Poppins:ital,wght@0,400;0,500;0,600;0,700;1,500;1,600&display=swap" rel="stylesheet">
<style>
:root{
  --navy:#1b2a3f;
  --blue:#2f86e8;
  --blue-light:#5aa2f0;
  --gold:#bba253;
  --gold-dark:#8d7a3c;
  --green:#22c51e;
  --grey-card:#f0f0f0;
  --line:#d9d9d9;
  --text:#1f2a36;
  --white:#fff;
}
*{box-sizing:border-box;margin:0;padding:0}
html,body{width:931px;height:1200px;overflow:hidden;background:var(--white);font-family:"Poppins",sans-serif;color:var(--text)}
.canvas{position:relative;width:931px;height:1200px;overflow:hidden}
.abs{position:absolute}

/* sidebar */
.sidebar{left:16px;top:16px;width:186px;height:1157px;background:var(--navy);border-radius:22px}
.brand{position:absolute;left:13px;top:13px;width:161px;height:82px;background:var(--white);border-radius:18px;text-align:center;padding-top:8px}
.brand-name{font-weight:700;font-size:23px;color:var(--navy);line-height:1.1}
.brand-sub{font-size:11px;color:var(--blue);line-height:1.45;margin-top:2px}
.role-label{position:absolute;left:13px;top:116px;color:var(--white);font-weight:600;font-size:12.5px}
.role-select{position:absolute;left:13px;top:139px;width:158px;height:32px;border:1px solid #3b4a60;border-radius:16px;color:var(--white);font-size:8.5px;padding:0 15px;display:flex;align-items:center;justify-content:space-between}
.nav{position:absolute;left:20px;top:201px;list-style:none}
.nav li{display:flex;align-items:center;height:42px;color:var(--white);font-size:10.5px;font-weight:500}
.nav svg{width:11px;height:11px;margin-right:12px;fill:var(--blue)}
.theme{position:absolute;left:18px;top:1066px;color:var(--white);font-size:10px;font-weight:500}
.theme-icons{position:absolute;left:18px;top:1088px;display:flex;gap:9px;align-items:center}
.version{position:absolute;left:18px;top:1116px;color:var(--white);font-size:10px;font-weight:600}
.version em{color:var(--gold);font-weight:500}

/* header */
.topbar{left:218px;top:16px;width:730px;height:73px;background:var(--navy);border-radius:28px 0 0 28px}
.search{position:absolute;left:305px;top:21px;width:254px;height:32px;background:var(--white);border-radius:16px;font-size:9px;display:flex;align-items:center;justify-content:space-between;padding:0 13px 0 15px}
.bell{position:absolute;left:573px;top:21px;width:32px;height:32px;border:1.5px solid var(--gold);border-radius:50%;display:flex;align-items:center;justify-content:center}
.avatar{position:absolute;left:615px;top:21px;width:32px;height:32px;background:var(--green);border-radius:50%;display:flex;align-items:center;justify-content:center}
.user{position:absolute;left:658px;top:28px;color:var(--white);font-size:12px}

/* sections */
.h2{font-size:16px;font-weight:600;color:#2c3440}
.divider{left:218px;width:696px;height:1px;background:var(--line)}

.due{top:146px;width:201px;height:98px;border-radius:6px;background:linear-gradient(135deg,#4d9cf0,#2f86e8);color:var(--white);padding:10px 11px}
.due h3{font-size:16px;font-weight:600;line-height:1.2}
.due p{font-size:11px;line-height:1.65;opacity:.85}
.badge{display:inline-block;margin-top:6px;background:var(--navy);color:var(--white);font-size:8px;font-weight:500;border-radius:10px;padding:3px 12px}
.due .num{position:absolute;right:23px;bottom:9px;font-size:30px;font-weight:700}
.due svg{position:absolute;right:22px;top:10px;width:42px;height:40px;fill:#8ec0f6}

.routine{width:342px;height:97px;background:var(--grey-card);border-radius:8px;padding:17px 11px}
.routine h3{font-size:15.5px;font-weight:600;color:var(--navy)}
.routine h3 em{font-size:12px;color:var(--blue);font-weight:500}
.routine p{font-size:10px;line-height:1.75;margin-top:7px;padding-left:31px;text-indent:-31px}
.routine b{color:var(--gold-dark);font-weight:600;margin-right:6px}

.stat{top:553px;width:222px;height:79px;border:1px solid #d4d4d4;border-radius:7px;padding:11px 11px}
.stat h3{font-size:15px;font-weight:600;color:var(--blue)}
.stat .val{font-size:32px;font-weight:700;color:var(--green);line-height:1.15}
.stat svg{position:absolute;right:15px;top:14px}

.report{top:717px;width:166px;height:97px;background:var(--gold);border-radius:7px;color:var(--white);padding:14px 11px}
.report svg.ic{height:26px}
.report .lbl{position:absolute;left:11px;bottom:10px;font-size:15.5px;font-weight:600;line-height:1.15}
.report .chev{position:absolute;right:15px;bottom:18px}

.chart{top:902px;width:342px;height:234px;border:1px solid #d4d4d4;border-radius:7px}
.chart svg{position:absolute;left:0;top:0}
</style>
</head>
<body>
<div class="canvas">

<aside class="abs sidebar">
  <div class="brand">
    <div class="brand-name">Zembrix</div>
    <div class="brand-sub">Company Management<br>Platform</div>
  </div>
  <div class="role-label">Role Selector</div>
  <div class="role-select"><span>Production A/B/C</span>
    <svg width="6" height="9" viewBox="0 0 6 9"><path d="M3 0 6 3.5H0zM3 9 0 5.5h6z" fill="#fff"/></svg></div>
  <ul class="nav">
    <li><svg viewBox="0 0 12 12"><path d="M6 1a6 6 0 0 0-6 6v3h12V7a6 6 0 0 0-6-6z"/></svg>Dashboard</li>
    <li><svg viewBox="0 0 12 12"><path d="M1 1h10v7H1zM0 9h12v2H0z"/></svg>Activities</li>
    <li><svg viewBox="0 0 12 12"><path d="M1 2h10v10H1zM3 0h1v3H3zM8 0h1v3H8z"/></svg>Planning</li>
    <li><svg viewBox="0 0 12 12"><path d="M2 0h6l3 3v9H2z"/></svg>Files</li>
    <li><svg viewBox="0 0 12 12"><text x="2" y="11" font-size="12" font-weight="700" fill="#2f86e8">$</text></svg>Costs</li>
    <li><svg viewBox="0 0 12 12"><path d="M1 0h10v12H1z"/></svg>Finances</li>
    <li><svg viewBox="0 0 12 12"><path d="M6 0l6 3v6l-6 3-6-3V3z"/></svg>Product Goods</li>
    <li><svg viewBox="0 0 12 12"><circle cx="6" cy="6" r="5"/></svg>API / Settings</li>
  </ul>
  <div class="theme">Theme toggle:</div>
  <div class="theme-icons">
    <svg width="12" height="12" viewBox="0 0 12 12"><circle cx="6" cy="6" r="3" fill="#e3b000"/><g stroke="#e3b000" stroke-width="1.2"><path d="M6 0v2M6 10v2M0 6h2M10 6h2M1.8 1.8l1.4 1.4M8.8 8.8l1.4 1.4M1.8 10.2l1.4-1.4M8.8 3.2l1.4-1.4"/></g></svg>
    <svg width="16" height="9" viewBox="0 0 16 9"><rect width="16" height="9" rx="4.5" fill="#22c51e"/><circle cx="11.5" cy="4.5" r="3" fill="#1b2a3f"/></svg>
    <svg width="12" height="12" viewBox="0 0 12 12"><path d="M7 0a6 6 0 1 0 5 8A5 5 0 0 1 7 0z" fill="#fff"/></svg>
  </div>
  <div class="version">Version badge: <em>v0.1 Prototype</em></div>
</aside>

<header class="abs topbar">
  <div class="search"><span>Search contracts, files, inventory</span>
    <svg width="12" height="12" viewBox="0 0 12 12"><circle cx="5" cy="5" r="3.8" stroke="#111" stroke-width="1.8" fill="none"/><path d="M8 8l3.3 3.3" stroke="#111" stroke-width="2"/></svg></div>
  <div class="bell"><svg width="11" height="12" viewBox="0 0 11 12"><path d="M5.5 0a3.5 3.5 0 0 0-3.5 3.5V7L0 9h11L9 7V3.5A3.5 3.5 0 0 0 5.5 0zM4 10h3a1.5 1.5 0 0 1-3 0z" fill="#fff"/></svg></div>
  <div class="avatar"><svg width="12" height="12" viewBox="0 0 12 12"><circle cx="6" cy="3.3" r="3" fill="#fff"/><path d="M0 12a6 5 0 0 1 12 0z" fill="#fff"/></svg></div>
  <div class="user">Marek</div>
</header>

<h2 class="abs h2" style="left:218px;top:111px">Due Dates</h2>
<svg class="abs" style="left:882px;top:116px" width="36" height="14" viewBox="0 0 36 14"><path d="M7 1 1 7l6 6M29 1l6 6-6 6" stroke="#333" stroke-width="1.5" fill="none"/></svg>

<div class="abs due" style="left:218px">
  <h3>Birthday</h3><p>R. Okafor<br>05 Sep 2025</p><span class="badge">Urgent</span>
  <svg viewBox="0 0 40 36"><rect x="2" y="12" width="36" height="8" rx="2"/><rect x="5" y="21" width="30" height="15" rx="2"/><path d="M20 12c-4-10-14-8-9 0zM20 12c4-10 14-8 9 0z"/><rect x="18" y="12" width="4" height="24" fill="#4d9cf0"/></svg>
  <span class="num">08</span>
</div>
<div class="abs due" style="left:435px">
  <h3>Passport</h3><p>T. Lindqvist<br>11 Oct 2025</p><span class="badge">Urgent</span>
  <svg viewBox="0 0 40 40"><rect x="6" y="0" width="30" height="40" rx="4"/><circle cx="21" cy="15" r="6" fill="#4d9cf0"/><path d="M11 31a10 8 0 0 1 20 0z" fill="#4d9cf0"/></svg>
  <span class="num">01</span>
</div>
<div class="abs due" style="left:651px">
  <h3>Contract</h3><p>D. Moreau<br>20 Oct 2025</p><span class="badge">Urgent</span>
  <svg viewBox="0 0 40 40"><rect x="18" y="2" width="14" height="22" rx="2" transform="rotate(45 25 13)"/><rect x="4" y="22" width="6" height="20" rx="2" transform="rotate(45 7 32)"/></svg>
  <span class="num">05</span>
</div>
<div class="abs due" style="left:866px">
  <h3>Residence</h3><p>K. Navarro<br>11 Oct 2025</p><span class="badge">Urgent</span>
</div>

<div class="abs divider" style="top:280px"></div>
<h2 class="abs h2" style="left:218px;top:298px">Daily Routine</h2>

<div class="abs routine" style="left:218px;top:334px">
  <h3>Send supplier RFQs <em>(Today)</em></h3>
  <p><b>Task</b>Neque porro quisquam est, qui dolorem ipsum quia dolor sit amet</p></div>
<div class="abs routine" style="left:572px;top:334px">
  <h3>Approve new contracts <em>(Today)</em></h3>
  <p><b>Task</b>Neque porro quisquam est, qui dolorem ipsum quia dolor sit amet</p></div>
<div class="abs routine" style="left:218px;top:442px">
  <h3>Check vehicle logs <em>(Tomorrow)</em></h3>
  <p><b>Task</b>Neque porro quisquam est, qui dolorem ipsum quia dolor sit amet</p></div>
<div class="abs routine" style="left:572px;top:442px">
  <h3>OPDS audit checklist <em>(This Week)</em></h3>
  <p><b>Task</b>Neque porro quisquam est, qui dolorem ipsum quia dolor sit amet</p></div>

<div class="abs stat" style="left:218px">
  <h3>Appointments</h3><div class="val">04</div>
  <svg width="30" height="34" viewBox="0 0 30 34"><rect x="1" y="4" width="28" height="29" rx="3" fill="none" stroke="#8ec0f6" stroke-width="2.5"/><rect x="1" y="4" width="28" height="7" fill="#8ec0f6"/><g fill="#8ec0f6"><rect x="6" y="15" width="4" height="4"/><rect x="13" y="15" width="4" height="4"/><rect x="20" y="15" width="4" height="4"/><rect x="6" y="22" width="4" height="4"/><rect x="13" y="22" width="4" height="4"/><rect x="20" y="22" width="4" height="4"/></g><rect x="7" y="0" width="3" height="7" fill="#8ec0f6"/><rect x="20" y="0" width="3" height="7" fill="#8ec0f6"/></svg>
</div>
<div class="abs stat" style="left:455px">
  <h3>Deadlines</h3><div class="val">03</div>
  <svg width="34" height="34" viewBox="0 0 34 34"><circle cx="17" cy="17" r="15" fill="none" stroke="#8ec0f6" stroke-width="3"/><path d="M17 8v10l6 5" stroke="#8ec0f6" stroke-width="3" fill="none"/></svg>
</div>
<div class="abs stat" style="left:692px">
  <h3>Weather</h3><div class="val">28°C</div>
  <svg width="44" height="30" viewBox="0 0 44 30"><path d="M10 30a9 9 0 0 1-1-18 12 12 0 0 1 23-2 10 10 0 0 1 2 20z" fill="#9ecbf7"/></svg>
</div>

<div class="abs divider" style="top:663px"></div>
<h2 class="abs h2" style="left:218px;top:681px">Reports Shortcut</h2>

<div class="abs report" style="left:218px">
  <svg class="ic" viewBox="0 0 34 26"><rect x="1" y="4" width="32" height="19" fill="none" stroke="#fff" stroke-width="2.5"/><circle cx="17" cy="13.5" r="5.5" fill="none" stroke="#fff" stroke-width="2"/></svg>
  <div class="lbl">Income<br>&amp; Expenses</div>
  <svg class="chev" width="8" height="14" viewBox="0 0 8 14"><path d="M1 1l6 6-6 6" stroke="#fff" stroke-width="1.6" fill="none"/></svg>
</div>
<div class="abs report" style="left:395px">
  <svg class="ic" viewBox="0 0 34 26"><path d="M2 0v24h32" stroke="#fff" stroke-width="2.5" fill="none"/><path d="M6 20l8-8 5 5 11-11" stroke="#fff" stroke-width="3" fill="none"/></svg>
  <div class="lbl">EBIT<br>(Target/Actual)</div>
  <svg class="chev" width="8" height="14" viewBox="0 0 8 14"><path d="M1 1l6 6-6 6" stroke="#fff" stroke-width="1.6" fill="none"/></svg>
</div>
<div class="abs report" style="left:571px">
  <svg class="ic" viewBox="0 0 24 30"><path d="M2 1h13l7 7v21H2z" fill="none" stroke="#fff" stroke-width="2.5"/><path d="M7 16h10M7 21h10" stroke="#fff" stroke-width="2"/></svg>
  <div class="lbl" style="bottom:18px">OPDS Docs</div>
  <svg class="chev" width="8" height="14" viewBox="0 0 8 14"><path d="M1 1l6 6-6 6" stroke="#fff" stroke-width="1.6" fill="none"/></svg>
</div>
<div class="abs report" style="left:748px">
  <svg class="ic" viewBox="0 0 30 26"><g fill="#fff"><rect x="0" y="1" width="5" height="5"/><rect x="8" y="1" width="22" height="5"/><rect x="0" y="10" width="5" height="5"/><rect x="8" y="10" width="22" height="5"/><rect x="0" y="19" width="5" height="5"/><rect x="8" y="19" width="22" height="5"/></g></svg>
  <div class="lbl">Loans<br>&amp; Inventory</div>
  <svg class="chev" width="8" height="14" viewBox="0 0 8 14"><path d="M1 1l6 6-6 6" stroke="#fff" stroke-width="1.6" fill="none"/></svg>
</div>

<div class="abs divider" style="top:847px"></div>
<h2 class="abs h2" style="left:218px;top:865px">Financial Overview</h2>

<div class="abs chart" style="left:218px">
  <svg width="342" height="234" viewBox="0 0 551 377" font-family="Poppins, sans-serif">
    <text x="21" y="47" font-size="23" font-weight="600" fill="#2f86e8">Income vs Expenses</text>
    <g font-size="14" fill="#222" text-anchor="end">
      <text x="54" y="85">$100</text><text x="54" y="112">$90</text><text x="54" y="139">$80</text><text x="54" y="166">$70</text><text x="54" y="193">$60</text><text x="54" y="220">$50</text><text x="54" y="247">$40</text><text x="54" y="274">$30</text><text x="54" y="301">$20</text><text x="54" y="329">$0</text>
    </g>
    <path d="M64 72v262h462" stroke="#333" stroke-width="1" fill="none"/>
    <g fill="#bba253">
      <rect x="75" y="116" width="30" height="218"/><rect x="162" y="204" width="30" height="130"/><rect x="252" y="116" width="30" height="218"/><rect x="340" y="86" width="30" height="248"/><rect x="425" y="275" width="30" height="59"/>
    </g>
    <g fill="#2f86e8">
      <rect x="105" y="167" width="30" height="167"/><rect x="192" y="167" width="30" height="167"/><rect x="282" y="129" width="30" height="205"/><rect x="370" y="167" width="30" height="167"/><rect x="455" y="167" width="30" height="167"/>
    </g>
    <g font-size="14" fill="#222" text-anchor="middle">
      <text x="104" y="355">2025</text><text x="191" y="355">2024</text><text x="280" y="355">2023</text><text x="368" y="355">2022</text><text x="457" y="355">2021</text>
    </g>
  </svg>
</div>

<div class="abs chart" style="left:572px">
  <svg width="342" height="234" viewBox="0 0 551 377" font-family="Poppins, sans-serif">
    <text x="21" y="47" font-size="23" font-weight="600" fill="#2f86e8">EBIT Target vs Actual</text>
    <g font-size="14" fill="#222" text-anchor="end">
      <text x="54" y="85">$100</text><text x="54" y="112">$90</text><text x="54" y="139">$80</text><text x="54" y="166">$70</text><text x="54" y="193">$60</text><text x="54" y="220">$50</text><text x="54" y="247">$40</text><text x="54" y="274">$30</text><text x="54" y="301">$20</text><text x="54" y="329">$0</text>
    </g>
    <g stroke="#444" stroke-width="0.8">
      <path d="M65 80h461M65 107h461M65 135h461M65 162h461M65 190h461M65 218h461M65 246h461M65 275h461M65 304h461M65 334h461"/>
      <path d="M65 72v262"/>
    </g>
    <polyline points="68,305 153,222 233,210 288,123 413,112 465,75" fill="none" stroke="#bba253" stroke-width="3"/>
    <polyline points="65,269 166,288 208,250 253,201 278,234 338,163 398,183 478,193 538,165" fill="none" stroke="#22c51e" stroke-width="3"/>
    <g font-size="14" fill="#222" text-anchor="middle">
      <text x="104" y="355">2025</text><text x="191" y="355">2024</text><text x="280" y="355">2023</text><text x="368" y="355">2022</text><text x="457" y="355">2021</text>
    </g>
  </svg>
</div>

</div>
</body>
</html>
```